Trendy Stylish Safety/Sports glasses polybag and box packaging

Polybag artwork required for safety glasses.
Polybag artwork required for sports glasses.
Packing box artwork required to tie in with polybag packaging.

Both bags to be similar, however one for safety glasses and one for sports glasses.
Maybe touch of different colours to differentiate.

Polybag Packaging for safety glasses.
1. Text to be white on black or vice versa, with a touch of yellow
2. Kermo logos to use, attached.
3. Front of bag to have clear vision panel on RH side
4. Bullet points can be on this clear vision panel.
5. Strapline to be on front of bag after ‘kerMosafety’ is COMFORT…STYLE…PROTECTION
6. Happy to have a touch of other colours on the packet to brighten up, make distinctive.
7. RH side at top on reverse of bag, bar code label to be attached, so this section to be left clear
8. Could have a few safety symbols on possibly.
9. Full text required on polybag is in file ‘safety packaging bag info.docx’

Polybag packaging for sports glasses

1. Text to be white on black or vice versa, with a touch of blue
5. Strapline to be on front of bag after ‘kerMosports’ is PERFORMANCE.…STYLE…PROTECTION
8. Full text required on polybag is in file ‘SPORTS packaging BAG Details.docx’
We havent decided on text for the reverse of this bag, however once we have the basic layout, we can add text at a later stage.

Cardboard packing/posting box for case.

We will use these boxes to pack and despatch our sports and safety glasses.

1. Two long sides of box to match polybag kerMo safety design.
Text required on safety sides of box
kerMosafety logo
COMFORT, STYLE, PROTECTION
2. Two long sides of box to match polybag kerMo sports design.
3. Text required on sports sides of box
kerMosports logo
PERFORMANCE, STYLE, PROTECTION
4. case box jpg has sizes required
Example of packing box picture attached.

Industry/Entity Type

Safety

```html
<!DOCTYPE html>
<html lang="en">
<head>
<meta charset="utf-8">
<title>kerMo eyewear packaging – polybags and case box</title>
<link rel="stylesheet" href="https://fonts.googleapis.com/css2?family=Allerta+Stencil&family=Oswald:wght@400;600;700&family=Roboto+Condensed:wght@400;700&display=swap">
<style>
  :root {
    --board: #a7a7a7;
    --ink: #0b0b0b;
    --paper: #ffffff;
    --safety-yellow: #f7d417;
    --sports-blue: #1b8fd2;
    --cut-line: #c8146e;
    --fold-line: #6b6b6b;
    --text-dark: #161616;
  }
  html, body {
    margin: 0;
    padding: 0;
    width: 1200px;
    height: 1000px;
    overflow: hidden;
    background: var(--board);
  }
  .artboard { display: block; width: 1200px; height: 1000px; }
  .cut { stroke: var(--cut-line); stroke-width: 0.8; }
  .fold { stroke: var(--fold-line); stroke-width: 0.5; fill: none; }
  .panel-black { fill: var(--ink); }
  .panel-white { fill: var(--paper); }
  .brand { font-family: "Oswald", sans-serif; font-weight: 700; fill: var(--paper); }
  .range-label { font-family: "Oswald", sans-serif; font-weight: 600; letter-spacing: 1px; }
  .range-safety { fill: var(--safety-yellow); }
  .range-sports { fill: var(--sports-blue); }
  .headline { font-family: "Allerta Stencil", sans-serif; font-size: 16.5px; fill: var(--text-dark); }
  .bullet { font-family: "Allerta Stencil", sans-serif; font-size: 10px; fill: var(--text-dark); }
  .strapline { font-family: "Oswald", sans-serif; font-weight: 700; fill: var(--paper); }
  .care-text { font-family: "Roboto Condensed", sans-serif; font-size: 5.2px; fill: var(--text-dark); }
  .care-title { font-family: "Roboto Condensed", sans-serif; font-size: 5.4px; font-weight: 700; fill: var(--text-dark); }
  .warning-label { font-family: "Roboto Condensed", sans-serif; font-size: 5.4px; font-weight: 700; fill: var(--paper); }
  .header-small { font-family: "Roboto Condensed", sans-serif; font-size: 5px; font-weight: 700; fill: var(--paper); }
  .sep-safety { fill: var(--safety-yellow); }
  .sep-sports { fill: var(--sports-blue); }
</style>
</head>
<body>
<svg class="artboard" viewBox="0 0 1200 1000" xmlns="http://www.w3.org/2000/svg">
  <defs>
    <radialGradient id="splash-yellow" cx="50%" cy="50%" r="60%">
      <stop offset="0%" stop-color="#f7d417" stop-opacity="0.95"/>
      <stop offset="55%" stop-color="#c9a90f" stop-opacity="0.45"/>
      <stop offset="100%" stop-color="#0b0b0b" stop-opacity="0"/>
    </radialGradient>
    <radialGradient id="splash-blue" cx="50%" cy="50%" r="60%">
      <stop offset="0%" stop-color="#1b8fd2" stop-opacity="0.95"/>
      <stop offset="55%" stop-color="#136a9c" stop-opacity="0.45"/>
      <stop offset="100%" stop-color="#0b0b0b" stop-opacity="0"/>
    </radialGradient>
  </defs>

  <!-- Sports polybag front -->
  <g class="polybag polybag-sports">
    <rect class="panel-white cut" x="111" y="30" width="172" height="445"/>
    <rect class="panel-black" x="111" y="30" width="172" height="73"/>
    <text class="brand" x="197" y="77" font-size="27" text-anchor="middle">kerMo</text>
    <text class="range-label range-sports" x="197" y="96" font-size="10" text-anchor="middle">SPORTS</text>
    <rect class="panel-black" x="111" y="103" width="52" height="324"/>
    <rect role="img" aria-label="Blue paint splash texture" x="111" y="103" width="26" height="150" fill="url(#splash-blue)"/>
    <g transform="translate(157,422) rotate(-90)">
      <text class="brand" x="0" y="0" font-size="46">kerMo</text>
      <text class="range-label" x="150" y="-4" font-size="26" fill="#ffffff">SPORTS</text>
    </g>
    <text class="headline" x="170" y="131">PERFORMANCE</text>
    <text class="headline" x="170" y="154">STYLE</text>
    <text class="headline" x="170" y="177">PROTECTION</text>
    <text class="bullet" x="168" y="364">+STYLISH DESIGN</text>
    <text class="bullet" x="168" y="383">+POLYCARBONATE LENS</text>
    <text class="bullet" x="168" y="402">+UV PROTECTION</text>
    <text class="bullet" x="168" y="421">+ANTI FOG COATED</text>
    <line class="fold" x1="111" y1="427" x2="283" y2="427"/>
  </g>

  <!-- Safety polybag front -->
  <g class="polybag polybag-safety">
    <rect class="panel-white cut" x="303" y="30" width="172" height="445"/>
    <rect class="panel-black" x="303" y="30" width="172" height="73"/>
    <text class="brand" x="389" y="77" font-size="27" text-anchor="middle">kerMo</text>
    <text class="range-label range-safety" x="389" y="96" font-size="10" text-anchor="middle">SAFETY</text>
    <rect class="panel-black" x="303" y="103" width="52" height="324"/>
    <rect role="img" aria-label="Yellow paint splash texture" x="303" y="103" width="28" height="324" fill="url(#splash-yellow)"/>
    <g transform="translate(349,422) rotate(-90)">
      <text class="brand" x="0" y="0" font-size="46">kerMo</text>
      <text class="range-label range-safety" x="150" y="-4" font-size="26">SAFETY</text>
    </g>
    <text class="headline" x="362" y="131">COMFORT</text>
    <text class="headline" x="362" y="154">STYLE</text>
    <text class="headline" x="362" y="177">PROTECTION</text>
    <text class="bullet" x="358" y="350">+IMPACT RESISTANT</text>
    <text class="bullet" x="358" y="364">+STYLISH DESIGN</text>
    <text class="bullet" x="358" y="378">+CE CERTIFIED</text>
    <text class="bullet" x="358" y="392">+POLYCARBONATE LENS</text>
    <text class="bullet" x="358" y="406">+UV PROTECTION</text>
    <text class="bullet" x="358" y="420">+ANTI FOG COATED</text>
    <line class="fold" x1="303" y1="427" x2="475" y2="427"/>
  </g>

  <!-- Safety polybag reverse -->
  <g class="polybag polybag-reverse">
    <rect class="panel-white cut" x="494" y="30" width="172" height="445"/>
    <rect class="panel-black" x="494" y="30" width="172" height="73"/>
    <g transform="translate(501,36) rotate(90)">
      <text class="header-small" x="0" y="0">COMFORT</text>
      <text class="header-small" x="0" y="-6">STYLE</text>
      <text class="header-small" x="0" y="-12">PROTECTION</text>
      <text class="header-small" x="0" y="-18">www.kermosafety.com</text>
    </g>
    <polyline points="595,30 610,45 640,45 660,62 666,62" fill="none" stroke="var(--safety-yellow)" stroke-width="0.8"/>
    <polyline points="620,103 640,82 666,82" fill="none" stroke="var(--safety-yellow)" stroke-width="0.8"/>
    <rect class="panel-white" x="565" y="47" width="48" height="16"/>

    <text class="care-title" x="500" y="115">EN166:2001</text>
    <text class="care-title" x="500" y="121">Taking care of your safety eyewear:</text>
    <text class="care-text" x="500" y="127">Store at normal room temperature in a box or locker.</text>
    <text class="care-text" x="500" y="133">Keep in the bag or case provided, away from other items.</text>
    <text class="care-text" x="500" y="139">Clean with warm soapy water, then dry with a soft lint free cloth.</text>
    <text class="care-text" x="500" y="145">Disinfect with a mild household cleaner when needed, then rinse</text>
    <text class="care-text" x="500" y="151">and dry. Check hinges and screws are tight before each use.</text>
    <text class="care-text" x="500" y="157">Scratched or damaged lenses and frames must be replaced at once.</text>
    <text class="care-text" x="500" y="163">Items worn out at the end of their useful life must be replaced.</text>

    <text class="care-title" x="500" y="196">Product Life:</text>
    <text class="care-text" x="500" y="202">If stored in good condition at an even room temperature they</text>
    <text class="care-text" x="500" y="208">will last many years but must be checked before each use.</text>
    <text class="care-text" x="500" y="214">Replace at any sign of wear or damage.</text>

    <text class="care-title" x="500" y="234">Product Markings:</text>
    <text class="care-text" x="500" y="240">If the symbols S, F or B are not common to both lens and frame,</text>
    <text class="care-text" x="500" y="246">the lower level applies to the complete eye protector.</text>

    <text class="care-title" x="500" y="266">SYMBOL</text>
    <text class="care-text" x="500" y="272">DESCRIPTION OF THE FIELD OF USE/MARKINGS</text>
    <text class="care-text" x="500" y="278">No symbol</text><text class="care-text" x="535" y="278">General purpose, low speed impacts (frame only)</text>
    <text class="care-text" x="500" y="284">S</text><text class="care-text" x="535" y="284">Increased robustness</text>
    <text class="care-text" x="500" y="290">F</text><text class="care-text" x="535" y="290">High speed particles, low energy impact</text>
    <text class="care-text" x="500" y="296">B</text><text class="care-text" x="535" y="296">High speed particles, medium energy impact</text>
    <text class="care-text" x="500" y="302">1</text><text class="care-text" x="535" y="302">Optical class 1</text>
    <text class="care-text" x="500" y="308">EN166</text><text class="care-text" x="535" y="308">European standard for personal eye protection</text>

    <rect class="panel-black" x="499" y="321" width="36" height="8"/>
    <text class="warning-label" x="502" y="327">WARNING:</text>
    <text class="care-text" x="502" y="336">+ Impacts may pass through to the wearer when worn over</text>
    <text class="care-text" x="506" y="342">prescription glasses, creating a hazard.</text>
    <text class="care-text" x="502" y="348">+ Use at room temperature only unless marked with the letter T.</text>
    <text class="care-text" x="506" y="354">Should skin irritation occur, stop use and seek medical advice.</text>

    <text class="care-title" x="500" y="372">Additional markings for tinted lenses</text>
    <text class="care-text" x="500" y="379">EN169</text><text class="care-text" x="528" y="379">Welding shades, identified by shade number</text>
    <text class="care-text" x="500" y="386">EN170</text><text class="care-text" x="528" y="386">Ultraviolet filters, code 2 or 3</text>
    <text class="care-text" x="500" y="393">EN171</text><text class="care-text" x="528" y="393">Infrared filters, code 4</text>
    <text class="care-text" x="500" y="400">EN172</text><text class="care-text" x="528" y="400">Sunglare filters, code 5 or 6</text>

    <text class="care-text" x="500" y="416">Made in Taiwan</text>
    <line class="fold" x1="494" y1="427" x2="666" y2="427"/>
  </g>

  <!-- Case box, long side (safety) -->
  <g class="box-side box-side-safety">
    <rect class="panel-black" x="707" y="180" width="406" height="258"/>
    <rect role="img" aria-label="Yellow paint splash texture" x="707" y="180" width="140" height="70" fill="url(#splash-yellow)"/>
    <rect role="img" aria-label="Yellow paint splash texture" x="1030" y="180" width="83" height="120" fill="url(#splash-yellow)"/>
    <rect role="img" aria-label="Yellow paint splash texture" x="880" y="180" width="170" height="40" fill="url(#splash-yellow)"/>
    <text class="brand" x="975" y="287" font-size="28" text-anchor="middle">kerMo</text>
    <text class="brand" x="716" y="377" font-size="58">kerMo</text>
    <text class="range-label range-safety" x="930" y="362" font-size="26">SAFETY</text>
    <line x1="716" y1="383" x2="1068" y2="383" stroke="var(--paper)" stroke-width="2"/>
    <text class="strapline" x="724" y="407" font-size="22" letter-spacing="0.5">COMFORT</text>
    <rect class="sep-safety" x="835" y="388" width="4" height="22"/>
    <text class="strapline" x="847" y="407" font-size="22" letter-spacing="0.5">STYLE</text>
    <rect class="sep-safety" x="922" y="388" width="4" height="22"/>
    <text class="strapline" x="933" y="407" font-size="22" letter-spacing="0.5">PROTECTION</text>
  </g>

  <!-- Case box dieline, safety -->
  <g class="dieline dieline-safety">
    <path class="panel-black cut" d="M112 505 Q112 495 122 495 L227 495 Q237 495 237 505 L237 615 L237 890 L237 955 L150 955 L150 935 L125 935 L125 955 L112 955 Z"/>
    <path class="panel-black cut" d="M237 615 L237 578 Q237 567 248 567 L300 567 L332 600 L332 615 Z"/>
    <path class="panel-black cut" d="M237 615 L332 615 L332 890 L237 890 Z"/>
    <path class="panel-black cut" d="M237 890 L332 890 L332 930 L318 955 L252 955 L237 930 Z"/>
    <path class="panel-black cut" d="M332 615 L458 615 L458 890 L332 890 Z"/>
    <path class="panel-black cut" d="M332 890 L458 890 L458 910 L425 948 L365 948 L332 910 Z"/>
    <path class="panel-black cut" d="M458 615 L458 578 Q458 567 469 567 L521 567 L555 600 L555 615 Z"/>
    <path class="panel-black cut" d="M458 615 L555 615 L555 890 L458 890 Z"/>
    <path class="panel-black cut" d="M458 890 L555 890 L555 930 L541 955 L473 955 L458 930 Z"/>
    <line class="fold" x1="112" y1="615" x2="555" y2="615"/>
    <line class="fold" x1="112" y1="890" x2="555" y2="890"/>

    <rect role="img" aria-label="Yellow paint splash texture" x="112" y="495" width="125" height="400" fill="url(#splash-yellow)"/>
    <rect role="img" aria-label="Yellow paint splash texture" x="332" y="615" width="90" height="275" fill="url(#splash-yellow)"/>

    <g transform="translate(200,640) rotate(90)"><text class="brand" font-size="40">kerMo</text></g>
    <g transform="translate(420,640) rotate(90)"><text class="brand" font-size="40">kerMo</text></g>

    <g transform="translate(291,885) rotate(-90)">
      <text class="brand" x="0" y="0" font-size="50">kerMo</text>
      <text class="range-label range-safety" x="158" y="-4" font-size="24">SAFETY</text>
    </g>
    <g transform="translate(318,885) rotate(-90)">
      <text class="strapline" x="0" y="0" font-size="18">COMFORT</text>
      <rect class="sep-safety" x="80" y="-16" width="3" height="18"/>
      <text class="strapline" x="90" y="0" font-size="18">STYLE</text>
      <rect class="sep-safety" x="142" y="-16" width="3" height="18"/>
      <text class="strapline" x="152" y="0" font-size="18">PROTECTION</text>
    </g>
    <g transform="translate(512,885) rotate(-90)">
      <text class="brand" x="0" y="0" font-size="50">kerMo</text>
      <text class="range-label range-safety" x="158" y="-4" font-size="24">SAFETY</text>
    </g>
    <g transform="translate(539,885) rotate(-90)">
      <text class="strapline" x="0" y="0" font-size="18">COMFORT</text>
      <rect class="sep-safety" x="80" y="-16" width="3" height="18"/>
      <text class="strapline" x="90" y="0" font-size="18">STYLE</text>
      <rect class="sep-safety" x="142" y="-16" width="3" height="18"/>
      <text class="strapline" x="152" y="0" font-size="18">PROTECTION</text>
    </g>
  </g>

  <!-- Case box dieline, sports -->
  <g class="dieline dieline-sports" transform="translate(482,0)">
    <path class="panel-black cut" d="M112 505 Q112 495 122 495 L227 495 Q237 495 237 505 L237 615 L237 890 L237 955 L150 955 L150 935 L125 935 L125 955 L112 955 Z"/>
    <path class="panel-black cut" d="M237 615 L237 578 Q237 567 248 567 L300 567 L332 600 L332 615 Z"/>
    <path class="panel-black cut" d="M237 615 L332 615 L332 890 L237 890 Z"/>
    <path class="panel-black cut" d="M237 890 L332 890 L332 930 L318 955 L252 955 L237 930 Z"/>
    <path class="panel-black cut" d="M332 615 L458 615 L458 890 L332 890 Z"/>
    <path class="panel-black cut" d="M332 890 L458 890 L458 910 L425 948 L365 948 L332 910 Z"/>
    <path class="panel-black cut" d="M458 615 L458 578 Q458 567 469 567 L521 567 L555 600 L555 615 Z"/>
    <path class="panel-black cut" d="M458 615 L555 615 L555 890 L458 890 Z"/>
    <path class="panel-black cut" d="M458 890 L555 890 L555 930 L541 955 L473 955 L458 930 Z"/>
    <line class="fold" x1="112" y1="615" x2="555" y2="615"/>
    <line class="fold" x1="112" y1="890" x2="555" y2="890"/>

    <rect role="img" aria-label="Blue paint splash texture" x="112" y="495" width="125" height="300" fill="url(#splash-blue)"/>
    <rect role="img" aria-label="Blue paint splash texture" x="332" y="615" width="90" height="200" fill="url(#splash-blue)"/>

    <g transform="translate(200,640) rotate(90)"><text class="brand" font-size="40">kerMo</text></g>
    <g transform="translate(420,640) rotate(90)"><text class="brand" font-size="40">kerMo</text></g>

    <g transform="translate(291,885) rotate(-90)">
      <text class="brand" x="0" y="0" font-size="50">kerMo</text>
      <text class="range-label range-sports" x="158" y="-4" font-size="24">SPORTS</text>
    </g>
    <g transform="translate(318,885) rotate(-90)">
      <text class="strapline" x="0" y="0" font-size="17">PERFORMANCE</text>
      <rect class="sep-sports" x="110" y="-15" width="3" height="17"/>
      <text class="strapline" x="119" y="0" font-size="17">STYLE</text>
      <rect class="sep-sports" x="168" y="-15" width="3" height="17"/>
      <text class="strapline" x="177" y="0" font-size="17">PROTECTION</text>
    </g>
    <g transform="translate(512,885) rotate(-90)">
      <text class="brand" x="0" y="0" font-size="50">kerMo</text>
      <text class="range-label range-sports" x="158" y="-4" font-size="24">SPORTS</text>
    </g>
    <g transform="translate(539,885) rotate(-90)">
      <text class="strapline" x="0" y="0" font-size="17">PERFORMANCE</text>
      <rect class="sep-sports" x="110" y="-15" width="3" height="17"/>
      <text class="strapline" x="119" y="0" font-size="17">STYLE</text>
      <rect class="sep-sports" x="168" y="-15" width="3" height="17"/>
      <text class="strapline" x="177" y="0" font-size="17">PROTECTION</text>
    </g>
  </g>
</svg>
</body>
</html>
```